Harbor Ridge Capital and Investments

Create a simple business card design using the logos attached. Make it similar but not exact to the reference photo. Brand guidelines are also included.

```html
<!DOCTYPE html>
<html lang="en">
<head>
<meta charset="utf-8">
<title>Harbor Ridge Capital – Business Card</title>
<link href="https://fonts.googleapis.com/css2?family=Alfa+Slab+One&family=Poppins:wght@400;600&display=swap" rel="stylesheet">
<style>
  :root {
    --backdrop: #6b6b6b;
    --navy: #020c2b;
    --navy-deep: #010924;
    --teal: #1d4a63;
    --teal-soft: #123049;
    --copper: #8a4a1c;
    --paper: #fafafa;
    --ink: #0d1433;
  }
  * { box-sizing: border-box; margin: 0; padding: 0; }
  html, body {
    width: 1200px; height: 800px; overflow: hidden;
    background: var(--backdrop);
    font-family: "Poppins", sans-serif;
  }
  .sheet {
    width: 1200px; height: 800px;
    display: flex; align-items: center; justify-content: center; gap: 24px;
  }
  .card {
    width: 560px; height: 320px; position: relative; overflow: hidden;
    box-shadow: 0 18px 40px rgba(0,0,0,.35);
    border-bottom: 3px solid var(--copper);
  }

  /* front */
  .card-front { background: var(--navy); }
  .front-pattern {
    position: absolute; inset: 0;
    background:
      radial-gradient(ellipse 190px 130px at 50% 50%, var(--navy-deep) 0%, rgba(1,9,36,.9) 55%, rgba(1,9,36,0) 100%),
      linear-gradient(210deg, var(--teal) 0%, var(--teal-soft) 30%, var(--navy) 60%, #0a1a3a 100%);
  }
  .front-brand {
    position: absolute; inset: 0;
    display: flex; flex-direction: column; align-items: center; justify-content: center; gap: 14px;
  }
  .brand-dot { width: 46px; height: 46px; border-radius: 50%; background: var(--copper); }
  .brand-name {
    font-family: "Alfa Slab One", serif; font-weight: 400;
    letter-spacing: 4px; text-transform: uppercase; text-align: center;
  }
  .card-front .brand-name { color: #ffffff; font-size: 30px; line-height: 1.2; }

  /* back */
  .card-back { background: var(--paper); display: flex; align-items: center; }
  .back-brand {
    width: 262px; padding-left: 28px;
    display: flex; flex-direction: column; align-items: center; gap: 12px;
    margin-top: 30px;
  }
  .card-back .brand-dot { width: 40px; height: 40px; }
  .card-back .brand-name { color: var(--ink); font-size: 25px; line-height: 1.25; }
  .divider { width: 3px; height: 150px; background: var(--ink); margin: -20px 24px 0 12px; }
  .contact { color: var(--ink); margin-top: -24px; }
  .person-name { font-family: "Alfa Slab One", serif; font-weight: 400; font-size: 22px; letter-spacing: 1px; line-height: 1; }
  .person-title { color: var(--copper); font-weight: 600; font-size: 12px; letter-spacing: 1px; margin: 4px 0 8px; }
  .address { font-size: 12px; line-height: 1.45; margin-bottom: 10px; }
  .contact-list { list-style: none; font-size: 12.5px; line-height: 1; }
  .contact-list li { display: flex; align-items: center; gap: 8px; margin-bottom: 8px; }
  .contact-list svg { width: 13px; height: 13px; fill: var(--copper); flex: none; }
</style>
</head>
<body>
<main class="sheet">
  <section class="card card-front">
    <div class="front-pattern" role="img" aria-label="Repeating embossed brand-symbol pattern in deep navy fading to teal toward the top right"></div>
    <div class="front-brand">
      <span class="brand-dot"></span>
      <p class="brand-name">Harbor Ridge<br>Capital</p>
    </div>
  </section>

  <section class="card card-back">
    <div class="back-brand">
      <span class="brand-dot"></span>
      <p class="brand-name">Harbor Ridge<br>Capital</p>
    </div>
    <div class="divider"></div>
    <div class="contact">
      <h1 class="person-name">DANA WHITLOCK</h1>
      <p class="person-title">PRESIDENT</p>
      <p class="address">48 Ledger Lane,<br>Austin, TX 78701</p>
      <ul class="contact-list">
        <li><svg viewBox="0 0 24 24"><path d="M6.6 10.8a15 15 0 0 0 6.6 6.6l2.2-2.2c.3-.3.7-.4 1-.2 1.1.4 2.3.6 3.6.6.6 0 1 .4 1 1V20c0 .6-.4 1-1 1A17 17 0 0 1 3 4c0-.6.4-1 1-1h3.5c.6 0 1 .4 1 1 0 1.3.2 2.5.6 3.6.1.3 0 .7-.2 1z"/></svg>(512) 555-0142</li>
        <li><svg viewBox="0 0 24 24"><path d="M2 5h20v14H2z M2 5l10 7 10-7"/></svg>hello@harborridgecap.com</li>
        <li><svg viewBox="0 0 24 24"><path d="M12 2a10 10 0 1 0 0 20 10 10 0 0 0 0-20zm6.9 6h-3a15 15 0 0 0-1.3-3.9A8 8 0 0 1 18.9 8zM12 4c.8 1.2 1.5 2.5 1.9 4h-3.8c.4-1.5 1.1-2.8 1.9-4zM4.3 14a8 8 0 0 1 0-4h3.4a16 16 0 0 0 0 4zm.8 2h3a15 15 0 0 0 1.3 3.9A8 8 0 0 1 5.1 16zm3-8h-3a8 8 0 0 1 4.3-3.9A15 15 0 0 0 8.1 8zM12 20c-.8-1.2-1.5-2.5-1.9-4h3.8c-.4 1.5-1.1 2.8-1.9 4zm2.3-6H9.7a14 14 0 0 1 0-4h4.6a14 14 0 0 1 0 4zm.3 5.9c.6-1.2 1-2.5 1.3-3.9h3a8 8 0 0 1-4.3 3.9zm1.7-5.9a16 16 0 0 0 0-4h3.4a8 8 0 0 1 0 4z"/></svg>www.harborridgecap.com</li>
      </ul>
    </div>
  </section>
</main>
</body>
</html>
```